Brinmoor Suites internet banner add

Seldovia Alaska -I need a fabulous UNIQUE web banner for our two locations Brinmoor Suites Harbor Location and Brinmoor Suites Central location
All suites have full Kitchens
Open year Round
We cater to vacationers - fishermen - hikers - and families
Classy upbeat modern design
The dimensions for the banner ads are:

300x250
OR
728x90

Target Market(s)

Alaska- Nautical

Industry/Entity Type

Vacation rentals

Requirements
Must have
• I would like the attached photo as background Brinmoor Suites - always follow the quiet shore with our phone number- email - and 2 websites

```html
<!DOCTYPE html>
<html lang="en">
<head>
<meta charset="utf-8">
<title>Brinmoor Suites – web banners</title>
<link rel="stylesheet" href="https://fonts.googleapis.com/css2?family=Oswald:wght@500&family=Roboto:wght@500;700;900&display=swap">
<style>
  :root {
    --board: #3b3f3c;
    --navy: #24395a;
    --sky-top: #2f86e0;
    --sky-pale: #e4edf5;
    --water: #2e6aa3;
    --trees: #2f4a2c;
    --trees-deep: #1f331f;
    --gold: #f2c12e;
    --white: #ffffff;
    --accent: #c8262e;
  }
  * { box-sizing: border-box; margin: 0; padding: 0; }
  html, body { width: 1200px; height: 960px; overflow: hidden; }
  body {
    background: var(--board);
    font-family: "Roboto", Arial, sans-serif;
    position: relative;
  }
  .banner { position: absolute; overflow: hidden; }
  .banner--rect { width: 360px; height: 300px; top: 144px; }
  .banner--rect.is-gold { left: 163px; }
  .banner--rect.is-white { left: 677px; }
  .banner--board { width: 874px; height: 108px; left: 163px; }
  .banner--board.is-gold { top: 503px; }
  .banner--board.is-white { top: 659px; }

  .scene { position: absolute; inset: 0; }
  .banner--rect .scene {
    background: linear-gradient(180deg,
      var(--sky-top) 0%, #8fbbe6 30%, var(--sky-pale) 44%,
      var(--water) 52%, #3f6f63 60%, var(--trees) 74%, var(--trees-deep) 100%);
  }
  .banner--board .scene {
    background:
      linear-gradient(90deg, rgba(255,255,255,.9) 0%, rgba(255,255,255,.75) 30%, rgba(255,255,255,0) 48%),
      linear-gradient(180deg, #7fb0df 0%, var(--sky-pale) 22%, var(--water) 40%, #3d6d5f 62%, var(--trees) 100%);
  }

  .brand {
    position: absolute; display: flex; align-items: center; gap: 10px;
    color: var(--navy); font-weight: 700; text-transform: uppercase;
  }
  .brand__mark { width: 14px; height: 14px; background: var(--navy); flex: none; }
  .banner--rect .brand { left: 0; right: 0; top: 56px; justify-content: center; font-size: 25px; letter-spacing: 3px; }
  .banner--board .brand { left: 22px; top: 40px; font-size: 22px; letter-spacing: 2px; }

  .tagline {
    position: absolute; color: var(--navy); font-weight: 900;
    text-transform: uppercase; letter-spacing: .4px; white-space: nowrap;
  }
  .banner--rect .tagline { left: 0; right: 0; top: 132px; text-align: center; font-size: 15px; }
  .banner--board .tagline { left: 345px; top: 19px; font-size: 14px; }

  .phone {
    position: absolute; font-family: "Oswald", "Arial Narrow", sans-serif;
    font-weight: 500; line-height: 1; white-space: nowrap;
    text-shadow: 0 2px 3px rgba(0,0,0,.55);
  }
  .is-gold .phone { color: var(--gold); }
  .is-white .phone { color: var(--white); }
  .banner--rect .phone { left: 0; right: 0; top: 165px; text-align: center; font-size: 38px; }
  .banner--board .phone { left: 345px; top: 40px; font-size: 48px; }

  .contacts {
    position: absolute; list-style: none; color: var(--white); font-weight: 700;
    text-shadow: 0 1px 2px rgba(0,0,0,.7); white-space: nowrap;
  }
  .banner--rect .contacts { left: 0; right: 0; top: 214px; text-align: center; font-size: 15px; line-height: 22px; }
  .banner--board .contacts { right: 24px; top: 44px; text-align: right; font-size: 13px; line-height: 17px; }
</style>
</head>
<body>

<section class="banner banner--rect is-gold" aria-label="Brinmoor Suites 300 by 250 banner, gold phone">
  <div class="scene" role="img" aria-label="Photo of a snowy volcano across blue water with evergreen trees in front"></div>
  <div class="brand"><span class="brand__mark"></span><span class="brand__name">Brinmoor Suites</span></div>
  <p class="tagline">Always follow the quiet shore</p>
  <p class="phone">907-555-0148</p>
  <ul class="contacts">
    <li>Brinmoor_Suites@mailbox.com</li>
    <li>CentralSuitesofBrinmoor.com</li>
    <li>BrinmoorHarborInn.com</li>
  </ul>
</section>

<section class="banner banner--rect is-white" aria-label="Brinmoor Suites 300 by 250 banner, white phone">
  <div class="scene" role="img" aria-label="Photo of a snowy volcano across blue water with evergreen trees in front"></div>
  <div class="brand"><span class="brand__mark"></span><span class="brand__name">Brinmoor Suites</span></div>
  <p class="tagline">Always follow the quiet shore</p>
  <p class="phone">907-555-0148</p>
  <ul class="contacts">
    <li>Brinmoor_Suites@mailbox.com</li>
    <li>CentralSuitesofBrinmoor.com</li>
    <li>BrinmoorHarborInn.com</li>
  </ul>
</section>

<section class="banner banner--board is-gold" aria-label="Brinmoor Suites 728 by 90 banner, gold phone">
  <div class="scene" role="img" aria-label="Wide photo of a snowy volcano across blue water with evergreen trees"></div>
  <div class="brand"><span class="brand__mark"></span><span class="brand__name">Brinmoor Suites</span></div>
  <p class="tagline">Always follow the quiet shore</p>
  <p class="phone">907-555-0148</p>
  <ul class="contacts">
    <li>Brinmoor_Suites@mailbox.com</li>
    <li>CentralSuitesofBrinmoor.com</li>
    <li>BrinmoorHarborInn.com</li>
  </ul>
</section>

<section class="banner banner--board is-white" aria-label="Brinmoor Suites 728 by 90 banner, white phone">
  <div class="scene" role="img" aria-label="Wide photo of a snowy volcano across blue water with evergreen trees"></div>
  <div class="brand"><span class="brand__mark"></span><span class="brand__name">Brinmoor Suites</span></div>
  <p class="tagline">Always follow the quiet shore</p>
  <p class="phone">907-555-0148</p>
  <ul class="contacts">
    <li>Brinmoor_Suites@mailbox.com</li>
    <li>CentralSuitesofBrinmoor.com</li>
    <li>BrinmoorHarborInn.com</li>
  </ul>
</section>

</body>
</html>
```